Business Card Design Project

I would like a business card created for a new company. This is a holding company that acts as my investment company. It holds real estate and service based companies. The name of the company is Sandorecca which is Italian for Evolution. Defined as development or growth.
We currently have no logo. I really like some of the "different" cards out there. Potentially metallic or grey/black. That looks premium/hi-end and unique. I am not sure if your design would be specific to the card stock I end with our just logo/design/font.
Real Estate

```html
<!DOCTYPE html>
<html lang="en">
<head>
<meta charset="utf-8">
<title>Sandorecca Business Card</title>
<link rel="stylesheet" href="https://fonts.googleapis.com/css2?family=Tenor+Sans&display=swap">
<style>
  :root {
    --page: #ffffff;
    --card: #ffffff;
    --card-shadow: rgba(0, 0, 0, 0.75);
    --ink: #111111;
    --accent: #e8141b;
    --brand-faint: #e6e6e6;
  }
  html, body {
    margin: 0;
    padding: 0;
    width: 1200px;
    height: 754px;
    overflow: hidden;
    background: var(--page);
  }
  .card {
    position: absolute;
    left: 33px;
    top: 49px;
    width: 1151px;
    height: 682px;
    background: var(--card);
    border-radius: 34px;
    box-shadow: 8px 10px 8px var(--card-shadow);
    font-family: "Tenor Sans", sans-serif;
    font-variant: small-caps;
    color: var(--ink);
    overflow: hidden;
  }
  .card * { margin: 0; position: absolute; line-height: 1; white-space: nowrap; }

  .brand-name {
    left: 0;
    width: 1151px;
    top: 322px;
    text-align: center;
    font-size: 84px;
    letter-spacing: 0.12em;
    color: var(--brand-faint);
  }

  .headline {
    left: 43px;
    top: 38px;
    font-size: 40px;
    font-weight: 400;
    letter-spacing: 0.3em;
  }

  .specialties {
    list-style: none;
    padding: 0;
    left: 225px;
    top: 135px;
  }
  .specialties li {
    position: relative;
    display: block;
    height: 65px;
    font-size: 40px;
    letter-spacing: 0.31em;
    padding-left: 28px;
  }
  .specialties li::before {
    content: "";
    position: absolute;
    left: 0;
    top: 19px;
    width: 9px;
    height: 9px;
    border-radius: 50%;
    background: var(--ink);
  }

  .note {
    left: 0;
    width: 1151px;
    top: 340px;
    text-align: center;
    font-size: 34px;
    letter-spacing: 0.275em;
    color: var(--accent);
  }
  .note span { position: static; display: block; line-height: 54px; }

  .contact-name, .contact-details { top: 554px; font-size: 34px; }
  .contact-name { left: 35px; letter-spacing: 0.18em; }
  .contact-details { left: 492px; }
  .contact-name span, .contact-details span { position: static; display: block; line-height: 55px; }
  .contact-phone { letter-spacing: 0.25em; }
  .contact-email { letter-spacing: 0.19em; }
</style>
</head>
<body>
  <div class="card">
    <p class="brand-name" aria-hidden="true">Sandorecca</p>

    <h1 class="headline">Add your text</h1>

    <ul class="specialties">
      <li>Use bullet points</li>
      <li>To highlight</li>
      <li>What you specialise in</li>
    </ul>

    <p class="note">
      <span>This area can be left blank to allow</span>
      <span>for appointment times, notes etc</span>
      <span>to be handwritten in</span>
    </p>

    <p class="contact-name">
      <span>Contact:</span>
      <span>Your Name</span>
    </p>

    <p class="contact-details">
      <span class="contact-phone">Phone: 5555-5555</span>
      <span class="contact-email">Email: info@sandorecca.com</span>
    </p>
  </div>
</body>
</html>
```